Business Card design for new private practice opening

I need a business card design for my new private practice with my new logo uploaded as a file
On the front the logo
On the back: maybe a small logo somewhere?
Priv. Doz. DDr. Corinna Vestaluk
Fachärztin für Allgemein- & Viszeralchirurgie
Address: xxx
Tel: xxx
Mobil:xxx
Webseite:xxx
Email:xxx

Contact Information for Business Card

See project description above for details

Requirements
Nice to have
• I would like the colors of the logo incorporated into the business card

```html
<!DOCTYPE html>
<html lang="de">
<head>
<meta charset="utf-8">
<title>Vestaluk Chirurgie – Visitenkarte</title>
<link rel="stylesheet" href="https://fonts.googleapis.com/css2?family=Lato:wght@400;700;900&display=swap">
<style>
  :root {
    --teal: #47b9b7;
    --white: #ffffff;
    --ink: #2c3a3a;
    --page: #e6e8e8;
  }
  * { margin: 0; padding: 0; box-sizing: border-box; }
  html, body { width: 1200px; height: 915px; overflow: hidden; }
  body {
    background: var(--page);
    font-family: "Lato", sans-serif;
    position: relative;
  }
  .card {
    position: absolute;
    width: 720px;
    height: 411px;
    border-radius: 26px;
    background: var(--teal);
    overflow: hidden;
    box-shadow: 0 6px 18px rgba(0,0,0,0.18);
  }
  .card--front { left: 60px; top: 40px; }
  .card--back { left: 420px; top: 464px; }

  /* Front */
  .brand-front {
    position: absolute;
    left: 120px;
    top: 110px;
    display: flex;
    align-items: center;
    gap: 34px;
  }
  .brand-front .brand-dot {
    width: 170px; height: 170px;
    border-radius: 50%;
    background: var(--white);
  }
  .brand-front .brand-name {
    color: var(--white);
    font-weight: 900;
    font-size: 58px;
    line-height: 1.02;
    letter-spacing: 1px;
    text-transform: uppercase;
  }

  /* Back */
  .brand-back {
    position: absolute;
    right: 40px;
    top: 40px;
    display: flex;
    align-items: center;
    gap: 10px;
  }
  .brand-back .brand-dot {
    width: 42px; height: 42px;
    border-radius: 50%;
    background: var(--white);
  }
  .brand-back .brand-name {
    color: var(--white);
    font-weight: 900;
    font-size: 15px;
    line-height: 1.05;
    text-transform: uppercase;
  }
  .divider {
    position: absolute;
    left: 70px; right: 40px;
    top: 212px;
    height: 1.5px;
    background: var(--ink);
  }
  .person {
    position: absolute;
    left: 70px;
    top: 150px;
    color: var(--ink);
  }
  .person .name { font-weight: 900; font-size: 27px; line-height: 1.1; }
  .person .role { font-weight: 700; font-size: 15.5px; margin-top: 3px; }
  .contacts {
    position: absolute;
    left: 80px;
    top: 228px;
    list-style: none;
    color: var(--ink);
    font-size: 19px;
  }
  .contacts li { display: flex; align-items: center; gap: 14px; height: 30px; }
  .contacts svg { width: 20px; height: 20px; fill: var(--ink); }
  .address {
    position: absolute;
    right: 40px;
    top: 226px;
    text-align: right;
    color: var(--ink);
    font-size: 17px;
    line-height: 1.45;
  }
  .footer-band { position: absolute; left: 0; bottom: 0; width: 720px; height: 90px; }
  .website {
    position: absolute;
    right: 40px;
    bottom: 22px;
    color: var(--ink);
    font-size: 17px;
  }
</style>
</head>
<body>

  <section class="card card--front" aria-label="Vorderseite">
    <div class="brand-front">
      <span class="brand-dot"></span>
      <span class="brand-name">Vestaluk<br>Chirurgie</span>
    </div>
  </section>

  <section class="card card--back" aria-label="Rückseite">
    <div class="brand-back">
      <span class="brand-dot"></span>
      <span class="brand-name">Vestaluk<br>Chirurgie</span>
    </div>

    <div class="person">
      <p class="name">Priv. Doz. DDr. Corinna Vestaluk</p>
      <p class="role">Fachärztin für Allgemein- &amp; Viszeralchirurgie</p>
    </div>
    <div class="divider"></div>

    <ul class="contacts">
      <li>
        <svg viewBox="0 0 24 24"><path d="M6.6 10.8a15.1 15.1 0 0 0 6.6 6.6l2.2-2.2a1 1 0 0 1 1-.25 11.4 11.4 0 0 0 3.6.57 1 1 0 0 1 1 1V20a1 1 0 0 1-1 1A17 17 0 0 1 3 4a1 1 0 0 1 1-1h3.5a1 1 0 0 1 1 1c0 1.25.2 2.46.57 3.6a1 1 0 0 1-.25 1z"/></svg>
        044-123 456 789
      </li>
      <li>
        <svg viewBox="0 0 24 24"><path d="M7 1h10a2 2 0 0 1 2 2v18a2 2 0 0 1-2 2H7a2 2 0 0 1-2-2V3a2 2 0 0 1 2-2zm0 3v14h10V4zm5 15.5a1 1 0 1 0 0 2 1 1 0 0 0 0-2z"/></svg>
        044-123 456 789
      </li>
      <li>
        <svg viewBox="0 0 24 24"><path d="M2 5h20v14H2zm2 2v.5l8 5 8-5V7zm0 2.8V17h16V9.8l-8 5z"/></svg>
        info@webname.com
      </li>
    </ul>

    <div class="address">
      421, Address line goes here<br>
      45452, Country name
    </div>

    <svg class="footer-band" viewBox="0 0 720 90" preserveAspectRatio="none" aria-hidden="true">
      <polygon points="0,74 410,58 420,46 720,30 720,90 0,90" fill="#ffffff"/>
      <polygon points="0,66 400,50 410,40 416,40 406,54 0,70" fill="#ffffff"/>
    </svg>
    <p class="website">www.websitename.com</p>
  </section>

</body>
</html>
```